A Recruitment Company Needs a Web Design that Expresses High Energy and Results

Our company, BrightLane Consultants, needs a web design for our recruiting business based in Asia (Taiwan). We provide recruitment services to many international companies. Our client base is as follows:
Hi-Tech - 60%
Healthcare and Consumer/FMCG - 15%
Industrial and Engineering - 15%
Banking and Finance - 10%

The website will be accessed by both clients and job seekers. As such, it should look professional, user-friendly and is interactive.

Sans Serif

add136
ffffff
000000

• Attached is the company's logo. the design mus be in line with it.

```html
<!DOCTYPE html>
<html lang="en">
<head>
<meta charset="utf-8">
<title>BrightLane Consultants</title>
<link href="https://fonts.googleapis.com/css2?family=Roboto:wght@300;400;500;700&display=swap" rel="stylesheet">
<style>
:root{
  --brand:#add136;
  --brand-dark:#8cb62a;
  --ink:#222222;
  --white:#ffffff;
  --dark:#1c1c1c;
  --card-yellow:#fbb516;
  --card-green:#7dbf42;
  --card-red:#f05a24;
  --card-blue:#3399d6;
  --accent-orange:#f7a81b;
  --muted:#8a8a8a;
  --tint:rgba(255,255,255,0.22);
}
*{margin:0;padding:0;box-sizing:border-box}
html,body{width:1014px;height:1200px;overflow:hidden;background:var(--white)}
body{font-family:'Roboto',Arial,sans-serif;color:var(--ink)}
.page{position:relative;width:1014px;height:1200px;overflow:hidden}

/* Header */
.site-header{position:absolute;left:0;top:0;width:1014px;height:84px;border-bottom:2px solid var(--brand)}
.brand{position:absolute;left:84px;top:18px;width:142px;height:50px;display:flex;flex-direction:column;justify-content:center;
  color:var(--brand-dark);font-weight:700;line-height:1.05}
.brand .name{font-size:20px}
.brand .tag{font-size:9px;letter-spacing:2.5px;text-transform:uppercase}
.phone{position:absolute;right:84px;top:12px;font-size:20px;font-weight:500;color:var(--ink)}
.main-nav{position:absolute;right:84px;top:54px;display:flex;gap:22px}
.main-nav a{font-size:10.5px;text-transform:uppercase;color:var(--brand-dark);text-decoration:none;padding-bottom:10px;letter-spacing:.2px}
.main-nav a.active{border-bottom:4px solid var(--brand);padding-bottom:6px}

/* Services */
.section-title{font-weight:300;font-size:28px;letter-spacing:.5px}
.services-title{position:absolute;left:84px;top:112px}
.service-card{position:absolute;color:var(--white);padding:12px 18px}
.service-card h3{font-weight:300;font-size:19px;line-height:1.15;letter-spacing:.5px}
.service-card p{font-size:10px;line-height:1.45;margin-top:6px;max-width:240px}
.service-card .art{position:absolute;left:18px;background:var(--tint);border-radius:4px}
.service-card .go{position:absolute;right:18px;width:22px;height:22px}
.card-hitech{left:84px;top:168px;width:271px;height:156px;background:var(--card-yellow)}
.card-health{left:84px;top:337px;width:271px;height:176px;background:var(--card-blue)}
.card-industrial{left:366px;top:168px;width:282px;height:288px;background:var(--card-green)}
.card-banking{left:659px;top:168px;width:272px;height:170px;background:var(--card-red)}

/* Overview */
.overview{position:absolute;left:0;top:545px;width:1014px;height:346px;background:var(--dark);color:var(--white)}
.overview .section-title{position:absolute;left:84px;top:28px}
.overview-item{position:absolute;top:84px;width:265px}
.overview-item .photo{width:265px;height:176px}
.overview-item h4{margin-top:20px;font-size:12px;font-weight:700;color:var(--accent-orange);text-transform:uppercase}
.overview-item p{margin-top:8px;font-size:10px;color:#dddddd}
.item-media{left:84px}
.item-media .photo{background:linear-gradient(135deg,#d9d4cc,#6b6a6e 60%,#2d2d33)}
.item-banking{left:375px}
.item-banking .photo{background:linear-gradient(160deg,#f0f0f0,#a9aab0 55%,#3a3a40)}
.item-retail{left:665px}
.item-retail .photo{background:linear-gradient(120deg,#c9c6bf,#ececea 50%,#4a4a50)}

/* Clients */
.clients-title{position:absolute;left:0;width:1014px;top:924px;text-align:center;color:#333}
.client{position:absolute;top:1004px;transform:translateX(-50%);font-size:26px;font-weight:400;color:var(--muted)}

/* Footer */
.site-footer{position:absolute;left:0;top:1087px;width:1014px;height:113px;background:var(--dark);color:var(--white);text-align:center}
.social{display:flex;justify-content:center;gap:16px;margin-top:33px}
.social span{font-size:9px;letter-spacing:.3px}
.copyright{margin-top:22px;font-size:10px}
</style>
</head>
<body>
<div class="page">

  <header class="site-header">
    <div class="brand"><span class="name">BrightLane</span><span class="tag">Consultants</span></div>
    <div class="phone">(123) 555 0142</div>
    <nav class="main-nav">
      <a href="#">Home</a>
      <a href="#">Products</a>
      <a href="#">About Us</a>
      <a href="#" class="active">Outsourcing</a>
      <a href="#">Contact Us</a>
    </nav>
  </header>

  <h2 class="section-title services-title">Our Services</h2>

  <article class="service-card card-hitech">
    <h3>Hi-Tech</h3>
    <p>Skilled people suitable for challenging positions in the Hi-Tech industry</p>
    <div class="art" style="top:92px;width:40px;height:44px" role="img" aria-label="Line illustration of a telephone handset"></div>
    <svg class="go" style="top:101px" viewBox="0 0 24 24" fill="none" stroke="#fff" stroke-width="1.6"><circle cx="12" cy="12" r="10"/><path d="M7 12h9M12 8l4 4-4 4"/></svg>
  </article>

  <article class="service-card card-health">
    <h3>Healthcare and<br>Consumer/FMCG</h3>
    <p>Offering both talent and expertise, and we know we have the perfect fit for your business</p>
    <div class="art" style="top:115px;width:46px;height:48px" role="img" aria-label="Line illustration of a telephone with a chat bubble"></div>
    <svg class="go" style="top:127px" viewBox="0 0 24 24" fill="none" stroke="#fff" stroke-width="1.6"><circle cx="12" cy="12" r="10"/><path d="M7 12h9M12 8l4 4-4 4"/></svg>
  </article>

  <article class="service-card card-industrial">
    <h3>Industrial and<br>Engineering</h3>
    <p>Superior in knowledge and vastly experienced for the precise expertise in producing cutting-edge solutions</p>
    <div class="art" style="top:184px;width:94px;height:84px" role="img" aria-label="Line illustration of a computer screen linked to a globe"></div>
    <svg class="go" style="top:217px" viewBox="0 0 24 24" fill="none" stroke="#fff" stroke-width="1.6"><circle cx="12" cy="12" r="10"/><path d="M7 12h9M12 8l4 4-4 4"/></svg>
  </article>

  <article class="service-card card-banking">
    <h3>Banking and Financial</h3>
    <p>Security and Reliability is an important aspect and we are bound to that by outsourcing immensely qualified individuals</p>
    <div class="art" style="top:110px;width:54px;height:44px" role="img" aria-label="Line illustration of a card reader device"></div>
    <svg class="go" style="top:121px" viewBox="0 0 24 24" fill="none" stroke="#fff" stroke-width="1.6"><circle cx="12" cy="12" r="10"/><path d="M7 12h9M12 8l4 4-4 4"/></svg>
  </article>

  <section class="overview">
    <h2 class="section-title">Services Overview</h2>
    <div class="overview-item item-media">
      <div class="photo" role="img" aria-label="Photo of a business team meeting around a table"></div>
      <h4>Hi-Tech and Media</h4>
      <p>Services for Media and Hi-Tech</p>
    </div>
    <div class="overview-item item-banking">
      <div class="photo" role="img" aria-label="Photo of a businesswoman standing before her colleagues"></div>
      <h4>Banking and Financial</h4>
      <p>Services in Banking and Financial sector</p>
    </div>
    <div class="overview-item item-retail">
      <div class="photo" role="img" aria-label="Photo of a presenter speaking to an audience in an office"></div>
      <h4>Retail and Healthcare</h4>
      <p>Healthcare related and Consumer services</p>
    </div>
  </section>

  <h2 class="section-title clients-title">Our Clients</h2>
  <div class="client" style="left:190px">Vertexa</div>
  <div class="client" style="left:404px">Onyx</div>
  <div class="client" style="left:612px">Northvale</div>
  <div class="client" style="left:826px">Lumen</div>

  <footer class="site-footer">
    <div class="social">
      <span>Facet</span><span>Chirp</span><span>Plusly</span><span>Streamo</span><span>Linkora</span>
    </div>
    <p class="copyright">Copyright goes here</p>
  </footer>

</div>
</body>
</html>
```